Rug Cleaning Web Design Project

We need a web design for our cleaning company. We currently have a web page but are not happy with its design. We currently offer fine rug cleaning,upholstery cleaning, and residential and commercial carpet cleanning. We also offer water damage restoration. For our rug cleaning services we offer : Enzyme treatments for pet contamination and odor removal, application of stain protection that is designed for the fine textiles used in rug construction, application of treatments designed to prevent moth damage and pads designed to be used under rugs.Our current web site is harborlinewash.example. We are intrested in a design with similar information to the web page of Velmora Rug Cleaners INC. We would like to use the colors that are present in our logo that will be uploaded with this description. We would also like this new page to be linked to our other address fibertendpro.example. We would like the deign to be visually attractive but not "too busy".
Updates

Please include pictures of rugs, or people washing rugs if possible. We do not offer maid type cleaning services. We would not be interested in designs including pictures depicting that type service. Thanks for your hard work on this project.

Dale Hutchins

Industry/Entity Type

Residential

Requirements
Must have
• This page must be viewable on smart phones and tablets.

```html
<!DOCTYPE html>
<html lang="en">
<head>
<meta charset="utf-8">
<meta name="viewport" content="width=device-width, initial-scale=1">
<title>Velmora Rug Cleaners</title>
<link rel="stylesheet" href="https://fonts.googleapis.com/css2?family=Open+Sans:wght@400;600;700&family=Lobster+Two:ital,wght@1,700&display=swap">
<style>
:root{
  --blue:#1d8fc4;
  --blue-dark:#15709c;
  --blue-light:#3aa7d8;
  --nav-dark:#2f3336;
  --ink:#333333;
  --muted:#555555;
  --red:#d3262c;
  --page:#f7f7f5;
  --footer:#222324;
  --footer-text:#d8d8d8;
  --footer-head:#3fb0e6;
  --rule:#c9c9c9;
}
*{margin:0;padding:0;box-sizing:border-box}
html,body{width:1200px;height:1125px;overflow:hidden}
body{background:var(--page);font-family:"Open Sans",Arial,sans-serif;color:var(--ink);position:relative}
.header{position:absolute;left:0;top:0;width:1200px;height:95px;background:linear-gradient(#ffffff,#eeeeee)}
.brand{position:absolute;left:129px;top:22px;display:flex;align-items:center;gap:10px}
.brand-mark{width:40px;height:40px;border-radius:50%;background:var(--blue)}
.brand-name{font-size:30px;font-weight:700;color:var(--nav-dark);line-height:1}
.brand-sub{font-size:10px;font-weight:700;color:var(--nav-dark);letter-spacing:2px;margin-top:4px}
.call{position:absolute;left:826px;top:12px;display:flex;align-items:center;gap:8px;font-size:12px;color:var(--muted)}
.call strong{font-size:17px;font-weight:400;color:var(--muted);margin-left:4px}
.call svg{width:20px;height:18px}
.nav{position:absolute;left:545px;top:46px;display:flex;height:36px;background:linear-gradient(var(--blue-light),var(--blue-dark))}
.nav a{display:block;padding:0 20px;line-height:36px;color:#fff;font-size:15px;text-decoration:none;border-right:1px solid rgba(255,255,255,.2)}
.nav a.current{background:linear-gradient(#4b5054,var(--nav-dark));padding:0 26px}
.nav a:last-child{padding-right:32px;border:none}
.hero{position:absolute;left:0;top:94px;width:1200px;height:490px;background:linear-gradient(180deg,#d9d4c9 0%,#b89d82 45%,#8a4a3a 70%,#c0816e 100%)}
.strip{position:absolute;left:0;top:584px;width:1200px;height:36px;background:linear-gradient(#e6e6e6,#f4f4f4)}
.thumbs{position:absolute;left:133px;top:535px;display:flex;gap:11px}
.thumb{width:80px;height:78px;border:3px solid #fff;box-shadow:0 1px 4px rgba(0,0,0,.35)}
.thumb.active{outline:2px solid var(--blue)}
.welcome{position:absolute;left:134px;top:648px;width:637px}
.welcome h1{font-size:18px;font-weight:400;color:var(--red)}
.award{position:absolute;right:0;top:-6px;display:flex;align-items:center;gap:6px}
.award b{font-size:34px;font-weight:400;color:#222;line-height:1}
.award span{display:block;font-size:11px;line-height:1.3;color:#444}
.award span:first-child{border-bottom:2px solid #222;color:#111}
.dash{margin-top:16px;border-top:1px dashed var(--rule)}
.welcome h2{font-family:"Lobster Two",cursive;font-style:italic;font-size:20px;line-height:1.25;color:#2a2a2a;margin-top:16px}
.welcome p{font-size:11.5px;line-height:1.5;color:var(--muted);margin-top:10px}
.services{position:absolute;left:830px;top:646px;width:236px;height:259px;background:#fff;border:5px solid var(--blue);border-top:none;box-shadow:0 2px 4px rgba(0,0,0,.15)}
.services h3{height:43px;margin:0 -5px;background:linear-gradient(var(--blue-light),var(--blue-dark));color:#fff;font-weight:400;font-size:17px;padding:12px 0 0 16px;display:flex;align-items:center;gap:8px}
.services h3 svg{width:16px;height:12px}
.services ul{list-style:none;margin-top:22px}
.services li{font-size:14px;color:#444;padding:7px 0 7px 36px;border-top:1px solid #e3e3e3;position:relative}
.services li::before{content:"";position:absolute;left:18px;top:13px;width:8px;height:10px;border-radius:50% 50% 50% 50%/60% 60% 40% 40%;background:#777}
.footer{position:absolute;left:0;top:943px;width:1200px;height:182px;background:var(--footer);color:var(--footer-text);font-size:11.5px}
.footer::before{content:"";position:absolute;left:1006px;top:0;border:10px solid transparent;border-top-color:var(--page)}
.col{position:absolute;top:30px}
.col h4{font-weight:400;font-size:14px;color:var(--footer-head);margin-bottom:10px}
.sitemap{left:134px}
.sitemap li{list-style:none;padding-left:18px;position:relative;line-height:21px}
.sitemap li::before{content:"";position:absolute;left:4px;top:8px;width:6px;height:6px;border-radius:50%;background:#fff}
.follow{left:262px}
.follow li{list-style:none;display:flex;align-items:center;gap:7px;line-height:23px}
.follow li i{width:13px;height:13px;background:#3c6fb3;display:inline-block}
.follow li:nth-child(2) i{background:#3ab3e0}
.follow li:nth-child(3) i{background:#e8852a}
.follow li:nth-child(4) i{background:#2a75b0}
.reviews{left:454px;width:200px}
.reviews p{color:#aaa;line-height:1.4;font-style:italic}
.reviews .who{color:#e46a5c;font-style:normal;margin-top:10px}
.contact{left:708px;width:240px}
.contact-body{display:flex;gap:12px}
.map{width:78px;height:88px;background:linear-gradient(135deg,#e7e3d6,#c9d7c0);flex:none}
.contact-lines div{display:flex;gap:8px;line-height:1.45;margin-bottom:8px}
.contact-lines svg{width:10px;height:14px;flex:none;margin-top:2px}
</style>
</head>
<body>
<header class="header">
  <div class="brand">
    <span class="brand-mark"></span>
    <div><div class="brand-name">Velmora Rug Cleaners</div><div class="brand-sub">HARBORLINE CLEANING, LLC</div></div>
  </div>
  <div class="call">
    <svg viewBox="0 0 20 18"><rect width="20" height="18" rx="4" fill="#d3262c"/><path d="M6 4c1 0 2 2 2 3s-1 1-1 2 2 3 3 3 1-1 2-1 3 1 3 2-1 2-2 2C9 15 5 10 5 6c0-1 0-2 1-2z" fill="#fff"/></svg>
    Call Us Today <strong>+ 91 9000 555 012</strong>
  </div>
  <nav class="nav">
    <a class="current" href="#">Home</a><a href="#">About Us</a><a href="#">Services</a><a href="#">Testimonials</a><a href="#">Contact Us</a>
  </nav>
</header>

<div class="hero" role="img" aria-label="Photo of a worker squeegeeing a patterned oriental rug in a bright rug-washing hall"></div>
<div class="strip"></div>
<div class="thumbs">
  <div class="thumb" role="img" aria-label="Photo of a rug being hand cleaned" style="background:linear-gradient(#6a7fa6,#3b4662)"></div>
  <div class="thumb active" role="img" aria-label="Photo of a rug being washed" style="background:linear-gradient(#d8d2c8,#9a4b3f)"></div>
  <div class="thumb" role="img" aria-label="Photo of a wooden floor cleaning" style="background:linear-gradient(#8a5a34,#4a2c18)"></div>
  <div class="thumb" role="img" aria-label="Photo of upholstery cleaning equipment" style="background:linear-gradient(#5c4a3c,#2c2420)"></div>
</div>

<main class="welcome">
  <h1>Welcome to the Velmora Rug Cleaners</h1>
  <div class="award"><b>#1</b><div><span>best in business award</span><span>consumers first choice</span></div></div>
  <div class="dash"></div>
  <h2>There are many variations of passages of Lorem Ipsum available, but the have suffered alteration in some form, by injected humour,</h2>
  <p>There are many variations of passages of Lorem Ipsum available, but the majority have suffered alteration in some form, by injected humour, or randomised words which don't look even slightly believable. If you are going to use a passage of Lorem Ipsum, you need to be sure there isn't anything embarrassing hidden in the middle of text. All the Lorem Ipsum generators on the Internet tend to repeat predefined chunks as necessary, making this the first true generator on the Internet.</p>
  <p>It uses a dictionary of over 200 Latin words, combined with a handful of model sentence structures, to generate Lorem Ipsum which looks reasonable. The generated Lorem Ipsum is therefore always free from repetition, injected humour, or non-characteristic words etc.</p>
</main>

<aside class="services">
  <h3><svg viewBox="0 0 16 12"><rect y="0" width="16" height="2" fill="#fff"/><rect y="5" width="16" height="2" fill="#fff"/><rect y="10" width="16" height="2" fill="#fff"/></svg>Our Services</h3>
  <ul>
    <li>Rug Cleaning</li>
    <li>Upholstery Cleaning</li>
    <li>Residential and Commercial</li>
    <li>Carpet Cleanning</li>
    <li>Water Damage</li>
  </ul>
</aside>

<footer class="footer">
  <div class="col sitemap"><h4>Site Map</h4><ul><li>Home</li><li>About Us</li><li>Services</li><li>Testimonials</li></ul></div>
  <div class="col follow"><h4>Follow Us</h4><ul><li><i></i>Follow Us on Chatterly</li><li><i></i>Follow Us on Tweetline</li><li><i></i>Subscribe on RSS</li><li><i></i>LinkCircle</li></ul></div>
  <div class="col reviews"><h4>Testimonials</h4><p>&ldquo; It is a long established fact that a reader will be distracted by the readable content of a page when looking. &rdquo;</p><p class="who">Marcus Elwin Trask</p></div>
  <div class="col contact"><h4>Contact Us</h4>
    <div class="contact-body">
      <div class="map" role="img" aria-label="Small street map showing the shop location"></div>
      <div class="contact-lines">
        <div><svg viewBox="0 0 10 14"><path d="M5 0a5 5 0 0 1 5 5c0 4-5 9-5 9S0 9 0 5a5 5 0 0 1 5-5z" fill="#fff"/><circle cx="5" cy="5" r="2" fill="#222"/></svg>Contrary to popular belief, Lorem random text. It has roots in.</div>
        <div><svg viewBox="0 0 10 14"><rect x="1" width="8" height="14" rx="1.5" fill="#fff"/><rect x="2.5" y="2" width="5" height="8" fill="#222"/></svg>+ 91 9000 555 012</div>
        <div><svg viewBox="0 0 10 14"><rect y="3" width="10" height="8" fill="#fff"/><path d="M0 3l5 4 5-4" stroke="#222" fill="none"/></svg>info@fibertendpro.example</div>
      </div>
    </div>
  </div>
</footer>
</body>
</html>
```